Healthy Lifestyle Vitamin Supplement Company needs a web site designed.

We are starting a new website for selling quality natural vitamins and supplements online plus providing news and information on healthy living. We DO NOT need any programming done for this site. Just the design in a layered photoshop file. This site needs to communicate that we are the authoritative source for healthy living and a trusted place to buy supplements and information on living a healthy lifestyle.

Triggers On page will be

Trigger set 1
Home - Shop By Brand - Top Sellers - Clearance - Help Center - My Favorites

Trigger set 2
Vitamins and Herbs - Natural Living - Aromatherapy - Coffee and Tea - Health and Beauty - Healthy Foods - Pet Health - Sports and Diet

Triggers Other
Login - Shopping Cart - Checkout - Track Order

Need a search bar in the design

Left side should be categories look at Brelvox.com for example of categories.

Name and domain name is Sunward Meadow Crest

Will also need a logo to go along with that.

Industry/Entity Type

It Company

```html
<!DOCTYPE html>
<html lang="en">
<head>
<meta charset="utf-8">
<title>Sunward Meadow Crest — Natural Vitamins &amp; Supplements</title>
<link href="https://fonts.googleapis.com/css2?family=Oswald:wght@400;500;700&family=Open+Sans:wght@400;600;700&display=swap" rel="stylesheet">
<style>
  :root{
    --green:#8fc13b;
    --green-dark:#6f9d24;
    --ink:#222222;
    --topbar:#2f2f2f;
    --wood:#3b302a;
    --wood-deep:#2e2520;
    --panel:#463b34;
    --price:#e2492d;
    --muted:#666666;
    --paper:#ffffff;
    --soft:#f2f2f2;
    --footer:#2b2522;
  }
  *{box-sizing:border-box;margin:0;padding:0}
  html,body{width:1200px;height:3251px;overflow:hidden}
  body{font-family:"Open Sans",Arial,sans-serif;color:var(--ink);background:var(--paper);position:relative}
  .head-font{font-family:"Oswald","Arial Narrow",sans-serif}

  /* top bar */
  .topbar{height:49px;background:var(--topbar);color:#ddd;font-size:13px;display:flex;align-items:center;justify-content:space-between;padding:0 95px}
  .topbar-links{display:flex;gap:34px;align-items:center}
  .topbar-links span{display:flex;align-items:center;gap:6px}

  /* header */
  .site-header{height:119px;display:flex;align-items:center;justify-content:space-between;padding:0 95px}
  .brand{display:flex;align-items:center;gap:14px}
  .brand-dot{width:54px;height:54px;border-radius:50%;background:var(--green)}
  .brand-name{font-size:30px;font-weight:600;color:var(--green-dark)}
  .main-nav{display:flex;gap:30px;align-items:center;font-family:"Oswald",sans-serif;font-weight:500;font-size:15px;text-transform:uppercase;letter-spacing:.3px}

  /* hero */
  .hero{position:relative;height:442px}
  .hero-photo{position:absolute;inset:0;background:linear-gradient(90deg,#3c2a24 0%,#58606a 35%,#6d7b8a 55%,#3d3430 100%)}
  .hero-packs{position:absolute;left:95px;top:110px;width:520px;height:250px;background:linear-gradient(90deg,#c94b4b,#9bc43a 50%,#c0223a);opacity:.85;border-radius:6px}
  .hero-copy{position:absolute;right:95px;top:110px;display:flex;flex-direction:column;align-items:center;width:420px}
  .hero-kicker{background:var(--green);color:#fff;font:700 30px "Oswald",sans-serif;padding:2px 16px;letter-spacing:1px}
  .hero-title{margin-top:10px;background:var(--green);border:4px solid #fff;color:#fff;font:700 66px/1.1 "Oswald",sans-serif;padding:0 18px;letter-spacing:1px}
  .hero-sub{margin-top:14px;color:#fff;font:700 34px "Oswald",sans-serif;letter-spacing:18px}

  /* section headings */
  .section-title{display:block;width:max-content;margin:0 auto;border:3px solid #333;padding:8px 26px;font:500 22px "Oswald",sans-serif;letter-spacing:1.5px;text-transform:uppercase}
  .section-title.on-dark{border-color:#fff;color:#fff}

  /* shop by category */
  .shop{height:935px;padding-top:72px}
  .category-nav{margin-top:36px;text-align:center;font-size:14px;color:#333}
  .category-nav b{font-weight:700}
  .category-nav i{font-style:normal;margin:0 7px;color:#999}
  .product-row{display:flex;justify-content:space-between;padding:0 140px;margin-top:74px}
  .product{width:280px;text-align:center}
  .product-shot{width:160px;height:205px;margin:0 auto;border-radius:14px}
  .product-name{margin-top:118px;font:500 17px "Oswald",sans-serif;text-transform:uppercase}
  .product-name::after{content:"";display:block;width:40px;height:2px;background:#bbb;margin:8px auto 0}
  .price{margin-top:14px;color:var(--price);font:700 17px "Open Sans",sans-serif}
  .product-desc{margin-top:12px;font-size:12px;line-height:1.7;color:var(--muted)}
  .shop-now{display:block;width:218px;height:53px;margin:56px auto 0;position:relative}
  .shop-now span{position:absolute;inset:0;display:flex;align-items:center;justify-content:center;color:#fff;font:700 22px "Oswald",sans-serif;letter-spacing:1px}

  /* blog */
  .blog{height:760px;background:linear-gradient(180deg,var(--wood),var(--wood-deep));padding-top:85px;position:relative}
  .post-grid{display:grid;grid-template-columns:repeat(3,300px);justify-content:space-between;row-gap:62px;padding:0 95px;margin-top:46px}
  .post-head{display:flex;align-items:center;gap:22px}
  .post-num{width:46px;height:46px;background:var(--green);color:#fff;font:700 28px "Oswald",sans-serif;display:flex;align-items:center;justify-content:center}
  .post-title{color:#fff;font:700 18px "Oswald",sans-serif;text-transform:uppercase}
  .post-head + .rule{width:40px;height:2px;background:#cfcfcf;margin:8px 0 0 68px}
  .post-text{margin-top:12px;font-size:12px;line-height:1.8;color:#e6e6e6}
  .read-more{margin-top:8px;font:700 11px "Open Sans",sans-serif;color:#fff;text-transform:uppercase}
  .promo{position:absolute;left:95px;right:95px;bottom:0;height:123px;display:flex}
  .promo-photo{width:420px;background:linear-gradient(90deg,#caa24a,#7a4b1c 60%,#3e2a14)}
  .promo-copy{flex:1;background:var(--green);color:#fff;padding:16px 22px;font-family:"Oswald",sans-serif}
  .promo-copy h3{font-size:23px;font-weight:700;line-height:1.25;text-transform:uppercase}
  .promo-copy p{font-size:12px;font-weight:700;text-transform:uppercase;letter-spacing:.4px}
  .promo-action{width:265px;background:var(--green-dark);display:flex;align-items:center;justify-content:center}
  .btn-outline{border:2px solid #fff;color:#fff;font:700 15px "Oswald",sans-serif;padding:8px 22px;text-transform:uppercase}

  /* why choose */
  .why{height:495px;padding-top:96px;position:relative}
  .why-card{position:absolute;left:95px;top:214px;display:flex;gap:5px}
  .why-photo{width:285px;height:217px;background:linear-gradient(135deg,#5a4030,#b99a72 60%,#6b5036);position:relative}
  .play{position:absolute;left:50%;top:50%;width:54px;height:54px;margin:-27px 0 0 -27px;border-radius:50%;background:#fff;display:flex;align-items:center;justify-content:center}
  .why-text{width:605px;height:217px;background:var(--soft);padding:28px 24px}
  .why-text h4{font:500 20px "Oswald",sans-serif;text-transform:uppercase}
  .why-text h4::after{content:"";display:block;width:40px;height:2px;background:#999;margin-top:8px}
  .why-text p{margin-top:18px;font-size:12px;line-height:1.8;color:var(--muted)}
  .slider-arrows{position:absolute;right:100px;top:214px;display:flex;gap:8px}
  .slider-arrows div{width:44px;height:44px;background:var(--green);display:flex;align-items:center;justify-content:center}

  /* services */
  .services{height:365px;background:var(--wood);display:flex;padding:0 95px}
  .service{flex:1;background:var(--panel);margin-bottom:50px;text-align:center}
  .service + .service{border-left:1px solid #3a302a}
  .service-head{height:95px;background:var(--green);display:flex;align-items:center;justify-content:center;gap:16px;color:#fff;font:700 20px "Oswald",sans-serif;text-transform:uppercase}
  .service-rule{width:40px;height:2px;background:#ddd;margin:35px auto 0}
  .service p{margin:18px auto 0;width:270px;font-size:12px;line-height:1.7;color:#e4e4e4}
  .pay-badges{display:flex;justify-content:center;gap:10px;margin-top:14px}
  .pay-badges span{width:50px;height:28px;background:#fff;border-radius:3px}
  .service .btn-outline{display:inline-block;margin-top:24px;font-size:13px;padding:6px 20px}

  /* footer */
  .site-footer{height:86px;background:var(--footer);color:#ddd;font-size:12px;display:flex;align-items:center;justify-content:space-between;padding:0 95px}
  .footer-links{display:flex;gap:22px;text-transform:uppercase;margin-left:80px}
  .social{display:flex;gap:9px}
  .social span{width:22px;height:22px;border-radius:50%;background:#fff}
</style>
</head>
<body>

<div class="topbar">
  <span>Dara Whitfield, welcome to our online store!</span>
  <div class="topbar-links">
    <span>Login</span>
    <span><svg width="11" height="11" viewBox="0 0 12 12"><circle cx="6" cy="3.5" r="3" fill="#ddd"/><path d="M0 12c0-4 3-5.5 6-5.5s6 1.5 6 5.5z" fill="#ddd"/></svg>My Account ▾</span>
    <span><svg width="13" height="11" viewBox="0 0 14 12"><path d="M0 1h3l2 7h7l2-5H4" fill="none" stroke="#ddd" stroke-width="1.5"/><circle cx="6" cy="10.5" r="1.3" fill="#ddd"/><circle cx="11" cy="10.5" r="1.3" fill="#ddd"/></svg>0 item</span>
    <span>Checkout</span>
  </div>
</div>

<header class="site-header">
  <div class="brand"><span class="brand-dot"></span><span class="brand-name">Sunward Meadow Crest</span></div>
  <nav class="main-nav">
    <span>Home</span><span>Shop by Brand</span><span>Top Sellers</span><span>Clearance</span><span>Help Center</span><span>My Favorites</span>
    <svg width="16" height="16" viewBox="0 0 16 16"><circle cx="6.5" cy="6.5" r="5" fill="none" stroke="#222" stroke-width="2"/><path d="M10.5 10.5l4.5 4.5" stroke="#222" stroke-width="2"/></svg>
  </nav>
</header>

<section class="hero">
  <div class="hero-photo" role="img" aria-label="Misty autumn forest at dusk"></div>
  <div class="hero-packs" role="img" aria-label="Three supplement drink pouches in orange, lime and cherry flavours"></div>
  <div class="hero-copy">
    <div class="hero-kicker">LOREM IPSUM DOLOR</div>
    <div class="hero-title">ACCUSANTIUM</div>
    <div class="hero-sub">UNDE</div>
  </div>
</section>

<section class="shop">
  <h2 class="section-title">Shop by Category</h2>
  <p class="category-nav">Vitamins and Herbs<i>|</i><b>Natural Living</b><i>|</i>Aromatherapy<i>|</i>Coffee And Tea<i>|</i>Health And Beauty<i>|</i>Healthy Foods<i>|</i>Pet Health<i>|</i>Sports And Diet</p>
  <div class="product-row">
    <article class="product">
      <div class="product-shot" role="img" aria-label="Brown bottle of herbal supplement with green label" style="background:linear-gradient(180deg,#2a2a2a 0 18%,#7aa43a 18% 80%,#3a2a1a 80%)"></div>
      <h3 class="product-name">Voluptatem fugit aut</h3>
      <div class="price">$130.00</div>
      <p class="product-desc">ipsum dolor <b>sit</b> amet ipsum fugit aut<br>us nemo rem ipsam quasi voluptatem</p>
    </article>
    <article class="product">
      <div class="product-shot" role="img" aria-label="Bottle of fish oil softgels with yellow and green label" style="background:linear-gradient(180deg,#c9a24a 0 16%,#2a2a2a 16% 30%,#e8b92c 30% 85%,#2a2a2a 85%)"></div>
      <h3 class="product-name">Voluptatem fugit aut</h3>
      <div class="price">$130.00</div>
      <p class="product-desc">ipsum dolor sit amet ipsum fugit aut<br>us nem <b>rem ipsam</b> quasi voluptatem</p>
    </article>
    <article class="product">
      <div class="product-shot" role="img" aria-label="Blue bottle of prostate health capsules" style="background:linear-gradient(180deg,#e8e8e8 0 14%,#1f3fb0 14% 90%,#e8e8e8 90%)"></div>
      <h3 class="product-name">Voluptatem fugit aut</h3>
      <div class="price">$130.00</div>
      <p class="product-desc">ipsum dolor sit amet <b>voluptatem</b> fugit aut<br>us nemo rem ipsam quasi voluptatem</p>
    </article>
  </div>
  <a class="shop-now">
    <svg width="218" height="53" viewBox="0 0 218 53"><polygon points="0,0 218,0 198,53 20,53" fill="var(--green)"/></svg>
    <span>SHOP NOW</span>
  </a>
</section>

<section class="blog">
  <h2 class="section-title on-dark">Lates News From Blog</h2>
  <div class="post-grid">
    <article><div class="post-head"><span class="post-num">1</span><h3 class="post-title">Amet voluptatem</h3></div><div class="rule"></div><p class="post-text">Lorem ipsum dolor sit amet rem illo omnis aperiam aut aperiam sed quis aperiam eaque verita unde enim accusantium laudantium totam rem</p><p class="read-more">Read more</p></article>
    <article><div class="post-head"><span class="post-num">2</span><h3 class="post-title">Amet voluptatem</h3></div><div class="rule"></div><p class="post-text">Lorem ipsum dolor sit amet rem illo omnis aperiam aut aperiam sed quis aperiam eaque verita unde enim accusantium laudantium totam rem</p><p class="read-more">Read more</p></article>
    <article><div class="post-head"><span class="post-num">3</span><h3 class="post-title">Amet voluptatem</h3></div><div class="rule"></div><p class="post-text">Lorem ipsum dolor sit amet rem illo omnis aperiam aut aperiam sed quis aperiam eaque verita unde enim accusantium laudantium totam rem</p><p class="read-more">Read more</p></article>
    <article><div class="post-head"><span class="post-num">4</span><h3 class="post-title">Amet voluptatem</h3></div><div class="rule"></div><p class="post-text">Lorem ipsum dolor sit amet rem illo omnis aperiam aut aperiam sed quis aperiam eaque verita unde enim accusantium laudantium totam rem</p><p class="read-more">Read more</p></article>
    <article><div class="post-head"><span class="post-num">5</span><h3 class="post-title">Amet voluptatem</h3></div><div class="rule"></div><p class="post-text">Lorem ipsum dolor sit amet rem illo omnis aperiam aut aperiam sed quis aperiam eaque verita unde enim accusantium laudantium totam rem</p><p class="read-more">Read more</p></article>
    <article><div class="post-head"><span class="post-num">6</span><h3 class="post-title">Amet voluptatem</h3></div><div class="rule"></div><p class="post-text">Lorem ipsum dolor sit amet rem illo omnis aperiam aut aperiam sed quis aperiam eaque verita unde enim accusantium laudantium totam rem</p><p class="read-more">Read more</p></article>
  </div>
  <div class="promo">
    <div class="promo-photo" role="img" aria-label="Cup of herbal tea with a lemon slice"></div>
    <div class="promo-copy">
      <h3>Lorem ipsum dolor sit ab<br>amet rem illo omnis aut</h3>
      <p>Accusantium laudantium laudantium sunt</p>
    </div>
    <div class="promo-action"><span class="btn-outline">View more</span></div>
  </div>
</section>

<section class="why">
  <h2 class="section-title">Why You Choose</h2>
  <div class="why-card">
    <div class="why-photo" role="img" aria-label="Herbal tablets scattered on a wooden table, video thumbnail">
      <span class="play"><svg width="20" height="22" viewBox="0 0 20 22"><polygon points="3,1 19,11 3,21" fill="#5a4030"/></svg></span>
    </div>
    <div class="why-text">
      <h4>Sed enim accusantium</h4>
      <p>Lorem ipsum dolor sit amet rem illo omnis aut aperiam quis aperiam eaque veritatis aut aperiam veritatis unde enim, sed enim accusantium laudantium totam rem laudantium sunt perspiciatis ipsam sed doloremque ......</p>
    </div>
  </div>
  <div class="slider-arrows">
    <div><svg width="14" height="18" viewBox="0 0 14 18"><path d="M11 2L4 9l7 7" fill="none" stroke="#fff" stroke-width="3"/></svg></div>
    <div><svg width="14" height="18" viewBox="0 0 14 18"><path d="M3 2l7 7-7 7" fill="none" stroke="#fff" stroke-width="3"/></svg></div>
  </div>
</section>

<section class="services">
  <div class="service">
    <div class="service-head"><svg width="30" height="30" viewBox="0 0 30 30"><rect x="3" y="6" width="24" height="18" rx="2" fill="none" stroke="#fff" stroke-width="2.5"/><rect x="3" y="11" width="24" height="4" fill="#fff"/></svg>Payment Method</div>
    <div class="service-rule"></div>
    <p>Lorem ipsum dolor sit amet, omnis aperiam sed quis aperiam veritatis</p>
    <div class="pay-badges"><span></span><span></span><span></span><span></span></div>
  </div>
  <div class="service">
    <div class="service-head"><svg width="38" height="26" viewBox="0 0 38 26"><rect x="1" y="2" width="22" height="16" fill="#fff"/><path d="M23 7h8l6 6v5H23z" fill="#fff"/><circle cx="8" cy="21" r="4" fill="#fff" stroke="var(--green)" stroke-width="2"/><circle cx="30" cy="21" r="4" fill="#fff" stroke="var(--green)" stroke-width="2"/></svg>Free Shipping</div>
    <div class="service-rule"></div>
    <p>Lorem ipsum dolor sit amet, omnis aperiam sed quis aperiam veritatis unde enim accusantium laudantium</p>
    <span class="btn-outline">Read more</span>
  </div>
  <div class="service">
    <div class="service-head"><svg width="24" height="24" viewBox="0 0 24 24"><circle cx="10" cy="10" r="7" fill="none" stroke="#fff" stroke-width="3"/><path d="M15 15l7 7" stroke="#fff" stroke-width="3"/></svg>Track Your Order</div>
    <div class="service-rule"></div>
    <p>Lorem ipsum dolor sit amet, omnis aperiam sed quis aperiam veritatis unde enim accusantium laudantium</p>
    <span class="btn-outline">Read more</span>
  </div>
</section>

<footer class="site-footer">
  <span>© 2014 <b>YOUR COMPANY</b>. ALL RIGHTS RESERVED.</span>
  <nav class="footer-links"><span>About us</span><span>Term and use</span><span>Privacy policy</span><span>FAQs</span><span>Contact us</span></nav>
  <div class="social"><span></span><span></span><span></span><span></span><span></span></div>
</footer>

</body>
</html>
```